New Business Cards for Organic Meat Farm

We need a business card designed for Quillhaven Farm, a meat farm in western MA. Our logo uses a hand-drawn woodcut (attached). Our color palette has been simply black and white (shown in notepad and picture of our food truck). While we are based out of western MA, we have ambitions to grow nationally, so our hope is for a classy and memorable card which will be printed on a premium quality stock from a printer like printkestrel.com.
Target Market(s)
consumers of quality meats, restauranteurs, partnering farms
Industry/Entity Type
Farming and prepared meat products
Contact Information for Business Card
Ardel Penrow, President/Owner, ardel@quillhavenfarm.com, mobile: 413-555-0172, phone: 413-555-0148, quillhavenfarm.com, facebook: @quillhavenfarm, instagram: @quillhavenfarmma
Colors
Designer to choose colors to be used in the design.
Look and feel

```html
<!DOCTYPE html>
<html lang="en">
<head>
<meta charset="utf-8">
<title>Quillhaven Farm — Business Card</title>
<link rel="stylesheet" href="https://fonts.googleapis.com/css2?family=Bebas+Neue&family=Roboto:wght@400&display=swap">
<style>
  :root {
    --page: #ffffff;
    --card: #033044;
    --ink: #ffffff;
    --rule: rgba(255,255,255,0.75);
  }
  * { margin: 0; padding: 0; box-sizing: border-box; }
  html, body { width: 1200px; height: 1200px; overflow: hidden; background: var(--page); }
  .canvas { position: relative; width: 1200px; height: 1200px; }
  .card {
    position: absolute; left: 352px; width: 496px; height: 283px;
    background: var(--card); color: var(--ink);
  }
  .card--front { top: 273px; }
  .card--back { top: 615px; }

  .brand-seal {
    position: absolute; width: 152px; height: 152px;
    border: 3px solid var(--ink); border-radius: 50%;
    display: flex; flex-direction: column; align-items: center; justify-content: center;
    font-family: "Bebas Neue", sans-serif; font-weight: 400; color: var(--ink);
    text-align: center; line-height: 0.95;
  }
  .card--front .brand-seal { left: 66px; top: 65px; }
  .card--back .brand-seal { left: 297px; top: 31px; }
  .brand-seal__name { font-size: 32px; letter-spacing: 0.5px; }
  .brand-seal__sub { font-size: 20px; letter-spacing: 4px; }

  .identity {
    position: absolute; width: 202px; text-align: center;
    font-family: "Bebas Neue", sans-serif; font-weight: 400; color: var(--ink);
  }
  .card--front .identity { left: 237px; top: 116px; }
  .card--back .identity { left: 269px; top: 197px; }
  .identity__rule {
    height: 1px;
    background: linear-gradient(90deg, transparent, var(--rule) 15%, var(--rule) 85%, transparent);
  }
  .identity__name { font-size: 37px; line-height: 37px; letter-spacing: 0.5px; padding-top: 2px; }
  .identity__title { font-size: 14px; line-height: 16px; margin-top: 4px; letter-spacing: 0.5px; }

  .contact-list {
    position: absolute; left: 32px; top: 160px; list-style: none;
    font-family: "Roboto", sans-serif; font-size: 12.5px; line-height: 15.2px; color: var(--ink);
  }
  .contact-list li { display: flex; align-items: center; gap: 5px; white-space: nowrap; }
  .contact-list svg { width: 10px; height: 10px; flex: none; }
</style>
</head>
<body>
<div class="canvas">

  <section class="card card--front">
    <div class="brand-seal">
      <span class="brand-seal__name">Quillhaven</span>
      <span class="brand-seal__sub">Farm</span>
    </div>
    <div class="identity">
      <div class="identity__rule"></div>
      <div class="identity__name">Ardel Penrow</div>
      <div class="identity__rule"></div>
      <div class="identity__title">President/Owner</div>
    </div>
  </section>

  <section class="card card--back">
    <ul class="contact-list">
      <li>
        <svg viewBox="0 0 10 10"><circle cx="5" cy="5" r="5" fill="#fff"/><rect x="2.3" y="3.2" width="5.4" height="3.6" fill="none" stroke="#033044" stroke-width="0.7"/><path d="M2.3 3.2 L5 5.3 L7.7 3.2" fill="none" stroke="#033044" stroke-width="0.7"/></svg>
        ardel@quillhavenfarm.com
      </li>
      <li>
        <svg viewBox="0 0 10 10"><circle cx="5" cy="5" r="5" fill="#fff"/><path d="M3 2.5 L4.2 2.3 L4.7 3.8 L4 4.3 Q4.6 5.6 5.8 6.1 L6.3 5.4 L7.7 5.9 L7.5 7.1 Q4.8 7.4 2.9 5 Q2.6 3.6 3 2.5 Z" fill="#033044"/></svg>
        413-555-0172
      </li>
      <li>
        <svg viewBox="0 0 10 10"><circle cx="5" cy="5" r="5" fill="#fff"/><path d="M3 2.5 L4.2 2.3 L4.7 3.8 L4 4.3 Q4.6 5.6 5.8 6.1 L6.3 5.4 L7.7 5.9 L7.5 7.1 Q4.8 7.4 2.9 5 Q2.6 3.6 3 2.5 Z" fill="#033044"/></svg>
        413-555-0148
      </li>
      <li>
        <svg viewBox="0 0 10 10"><circle cx="5" cy="5" r="5" fill="#fff"/><g fill="none" stroke="#033044" stroke-width="0.6"><circle cx="5" cy="5" r="3"/><ellipse cx="5" cy="5" rx="1.3" ry="3"/><path d="M2 5 H8 M2.5 3.5 H7.5 M2.5 6.5 H7.5"/></g></svg>
        quillhavenfarm.com
      </li>
      <li>
        <svg viewBox="0 0 10 10"><circle cx="5" cy="5" r="5" fill="#fff"/></svg>
        @quillhavenfarm
      </li>
      <li>
        <svg viewBox="0 0 10 10"><circle cx="5" cy="5" r="5" fill="#fff"/></svg>
        @quillhavenfarmma
      </li>
    </ul>

    <div class="brand-seal">
      <span class="brand-seal__name">Quillhaven</span>
      <span class="brand-seal__sub">Farm</span>
    </div>
    <div class="identity">
      <div class="identity__rule"></div>
      <div class="identity__name">Ardel Penrow</div>
      <div class="identity__rule"></div>
      <div class="identity__title">President/Owner</div>
    </div>
  </section>

</div>
</body>
</html>
```